New logo and packaging for Chicago based skincare company

Venmira needs a new logo and packaging to help in marketing our new anti-aging skincare line.

About Us
We're quirky, skin-obsessed beauty geeks with a knack for research and a love for all things skincare. Our ambition to create REAL products with exotic ingredients inspired the name Venmira which translates to peau + jolie meaning beautiful skin in french.

Our Products
We strive to do it differently. We develop high potency, natural skincare products using top of the line, novel ingredients imported from all over the globe. Our products are made in the USA and free from gluten, parabens, sulfates, and useless fillers that can't deliver.
Price range: $25-75 (moderate)

LOGO
Open to any color/typography except red and purple. Should also be: modern, feminine, cultured, neutral, vibrant, simple, timeless, and sophisticated

LABEL
Logo placed on label, but should not be the focal point of product. EGF SERUM should grab attention of quick glancers
The ideal label design pairs neutrals with brights while achieving balance between minimalism and complexity.
Incorporates some sort of unconventionality, boldness, or uniqueness without adding distraction.

Color: Mostly white or silver background with splash of color (no purple, light pinks, or red). See attached kraft color chart for direction. Bright blues (teal, cobalt, navy, sky blue, and greens are ideal)

Target Market(s)

Target audience: Socially and health conscious women, cultured, ages 25-60, seeks high quality natural products with effective ingredients.

Industry/Entity Type

Skin Care Product

Logo Text

Venmira

Font styles to use
Other font styles liked:
• Open

Colors
f6f6f6
ffffff
fdfdfd
eeeeee
fbfbfb
0255a3
3176b5
33a6d7
86cfc6

Requirements
Must have
• Packaging includes:
• 1 oz amber glass bottles with white dropper - see attached image
• Dimensions: 1.25" width by 4.1" height
• Label should wrap around bottle similar to peptide complex image and includes ingredient list; Logo should be not focal point of label
• Green (peptide complex) label shows ideal clarity
• "NuGlint" can be written in several different ways, feel free to get creative
• Label Text:
• EGF
• NUGLINT
• SERUM
• Anti-aging Skin firming Scar removal
• 1 FL OZ (30ml)
• Ingredients:
• Hamamelis Virginiana (Witch Hazel) Water, Aqua (Water), Alcohol, Glycerin, Polysorbate 20, rh-Oligopeptide-1(EGF), Caprooyl Tetrapeptide-3, Cocos Nucifera (Coconut) Fruit Juice, Lavandula Angustifolia (Lavender) Oil, Citrus
• Paradisi (Pink Grapefruit) Peel Oil*, Citrus Aurantium Dulcis (Orange) Peel Oil*, Santalum Austrocaledonicum (Sandalwood) Wood Oil, Boswellia Carterii (Frankincense) Oil, Rosa Damascena Flower Oil, Dextran, Xanthan Gum,
• Gluconolactone, Sodium Benzoate
• Directions:
• Apply a small amount of EGF serum to clean skin once or twice daily. Allow to dry. Can be used both morning and night, and under makeup. Follow with moisturizer.
• Caution: For external use only. Use only as directed. Avoid contact with eyes. If contact occurs, rinse well with water.
• Distributed by Venmira, LLC
• Halden Ridge, Ohio 46398
• Made in USA, FDA Registered lab (please use symbols for these)
Nice to have
• Either or: White space, silver, boldness, numbers, kraft colors (see attached) shapes, geometric patterns, minimalism
• Label: Incorporate shapes and dimensions with minimal/bare background
• Open to handwritten fonts if clear and easy to read
Should not have
• No more than 3-4 colors, look too busy, cursive fonts

```html
<!DOCTYPE html>
<html lang="en">
<head>
<meta charset="utf-8">
<title>Venmira – EGF NuGlint Serum Labels</title>
<link rel="stylesheet" href="https://fonts.googleapis.com/css2?family=Tinos:wght@400;700&display=swap">
<style>
  :root {
    --page: #ffffff;
    --ink: #1a1a1a;
    --soft-ink: #8a8a8a;
    --label-white: #ffffff;
    --label-silver: #e4e4e4;
    --slate: #46515b;
    --amber-dark: #7d4212;
    --amber-light: #b2651f;
    --on-amber: #ffffff;
    --on-amber-soft: rgba(255, 255, 255, 0.55);
  }
  * { margin: 0; padding: 0; box-sizing: border-box; }
  html, body { width: 1200px; height: 806px; overflow: hidden; background: var(--page); }
  .canvas { position: relative; width: 1200px; height: 806px; }

  .brand-title {
    position: absolute; top: 34px; left: 0; width: 100%;
    text-align: center;
    font-family: "Tinos", serif; font-weight: 400;
    font-size: 52px; color: var(--ink); letter-spacing: 2px;
  }

  .label {
    position: absolute; top: 392px; width: 181px; height: 228px;
    background: linear-gradient(180deg, var(--label-silver) 0%, var(--label-white) 45%, var(--label-silver) 100%);
    border: 1px solid #cfcfcf;
    color: var(--ink);
    font-family: "Tinos", serif;
    text-align: center;
  }
  .label-frame {
    position: absolute; inset: 6px 5px;
    border: 2px solid var(--ink);
  }
  .label-frame::after {
    content: ""; position: absolute; inset: 3px;
    border: 0.6px solid var(--ink);
  }
  .line { position: absolute; left: 0; width: 100%; white-space: nowrap; }

  .egf-mark { top: 30px; font-size: 56px; line-height: 1; letter-spacing: -1px; }
  .product-line { top: 89px; font-size: 12px; letter-spacing: 0.3px; }
  .claim { font-size: 15.5px; letter-spacing: 1.5px; color: var(--soft-ink); }
  .claim-1 { top: 110px; }
  .claim-2 { top: 129px; }
  .claim-3 { top: 148px; }
  .volume { top: 170px; font-size: 9px; letter-spacing: 1.3px; }
  .wordmark { top: 189px; font-size: 15px; font-weight: 400; letter-spacing: 0.5px; }

  .label--serif .product-line { top: 44px; font-size: 12.5px; }
  .label--serif .serum-mark { top: 56px; font-size: 31px; font-weight: 400; letter-spacing: 1px; line-height: 1; }
  .label--serif .claim-1 { top: 97px; }
  .label--serif .claim-2 { top: 116px; }
  .label--serif .claim-3 { top: 135px; }
  .label--serif .volume { top: 161px; }
  .label--serif .wordmark { top: 184px; }

  .label--slate {
    background: linear-gradient(180deg, var(--slate) 0%, #6c7883 30%, #c9ced2 62%, var(--label-white) 85%);
  }
  .label--slate .product-line { top: 38px; color: #2b3238; }
  .label--slate .serum-mark { top: 50px; color: #22292f; }
  .label--slate .claim { color: #7b8086; }
  .label--slate .claim-1 { top: 91px; }
  .label--slate .claim-2 { top: 110px; }
  .label--slate .claim-3 { top: 129px; }
  .label--slate .volume { top: 155px; }
  .label--slate .wordmark { top: 179px; }

  .label--amber {
    background: linear-gradient(180deg, var(--amber-dark) 0%, var(--amber-light) 55%, var(--amber-dark) 100%);
    border-color: var(--on-amber);
    color: var(--on-amber);
  }
  .label--amber .label-frame,
  .label--amber .label-frame::after { border-color: var(--on-amber); }
  .label--amber .claim { color: var(--on-amber-soft); }

  .label--back { text-align: left; }
  .back-copy {
    position: absolute; top: 13px; left: 13px; right: 13px;
    font-size: 5.6px; line-height: 1.18; font-weight: 700;
    text-transform: uppercase; letter-spacing: 0.1px;
  }
  .back-copy p { margin-bottom: 5px; }
  .back-badges {
    position: absolute; right: 12px; bottom: 18px;
    display: flex; gap: 4px; align-items: center;
  }
</style>
</head>
<body>
<main class="canvas">
  <h1 class="brand-title">venmira</h1>

  <section class="label label--classic" style="left:34px;">
    <div class="label-frame"></div>
    <div class="line egf-mark">EGF</div>
    <div class="line product-line">NUGLINT SERUM</div>
    <div class="line claim claim-1">ANTI–AGING</div>
    <div class="line claim claim-2">SKIN FIRMING</div>
    <div class="line claim claim-3">SCAR REMOVAL</div>
    <div class="line volume">1FL OZ (30ML)</div>
    <div class="line wordmark">venmira</div>
  </section>

  <section class="label label--back" style="left:286px;">
    <div class="label-frame"></div>
    <div class="back-copy">
      <p>Ingredients:<br>Hamamelis Virginiana (Witch Hazel) Water, Aqua (Water), Alcohol, Glycerin, Polysorbate 20, rh-Oligopeptide-1(EGF), Caprooyl Tetrapeptide-3, Cocos Nucifera (Coconut) Fruit Juice, Lavandula Angustifolia (Lavender) Oil, Citrus Paradisi (Pink Grapefruit) Peel Oil*, Citrus Aurantium Dulcis (Orange) Peel Oil*, Santalum Austrocaledonicum (Sandalwood) Wood Oil, Boswellia Carterii (Frankincense) Oil, Rosa Damascena Flower Oil, Dextran, Xanthan Gum, Gluconolactone, Sodium Benzoate</p>
      <p>Directions:<br>Apply a small amount of EGF serum to clean skin once or twice daily. Allow to dry. Can be used both morning and night, and under makeup. Follow with moisturizer.</p>
      <p>Caution:<br>For external use only. Use only as directed. Avoid contact with eyes. If contact occurs, rinse well with water.</p>
      <p>Distributed by Venmira, LLC<br>Halden Ridge, Ohio 46398</p>
    </div>
    <svg class="back-badges" width="62" height="26" viewBox="0 0 62 26" role="img" aria-label="Registered lab and made in USA marks">
      <rect x="1" y="6" width="30" height="16" fill="#1a1a1a"/>
      <circle cx="48" cy="13" r="12" fill="none" stroke="#1a1a1a" stroke-width="2"/>
    </svg>
  </section>

  <section class="label label--serif" style="left:546px;">
    <div class="label-frame"></div>
    <div class="line product-line">– EGF NUGLINT –</div>
    <div class="line serum-mark">SERUM</div>
    <div class="line claim claim-1">ANTI–AGING</div>
    <div class="line claim claim-2">SKIN FIRMING</div>
    <div class="line claim claim-3">SCAR REMOVAL</div>
    <div class="line volume">1FL OZ (30ML)</div>
    <div class="line wordmark">venmira</div>
  </section>

  <section class="label label--serif label--slate" style="left:770px;">
    <div class="label-frame"></div>
    <div class="line product-line">– EGF NUGLINT –</div>
    <div class="line serum-mark">SERUM</div>
    <div class="line claim claim-1">ANTI–AGING</div>
    <div class="line claim claim-2">SKIN FIRMING</div>
    <div class="line claim claim-3">SCAR REMOVAL</div>
    <div class="line volume">1FL OZ (30ML)</div>
    <div class="line wordmark">venmira</div>
  </section>

  <section class="label label--amber" style="left:984px;">
    <div class="label-frame"></div>
    <div class="line egf-mark">EGF</div>
    <div class="line product-line">NUGLINT SERUM</div>
    <div class="line claim claim-1">ANTI–AGING</div>
    <div class="line claim claim-2">SKIN FIRMING</div>
    <div class="line claim claim-3">SCAR REMOVAL</div>
    <div class="line volume">1FL OZ (30ML)</div>
    <div class="line wordmark">venmira</div>
  </section>
</main>
</body>
</html>
```